Redesign of page from emergency manual

Please redesign this PDF to look better. Please don't include any stock photos. It must be legible. Making some words bold is probably a good idea.

Here are some things I like :

https://tarrowbooks.com.au/collections/frontpage/products/the-plk-v2-ebook

https://img-cd.vostramediafiles.com/qa-ejkwPLOTYY_SuCKbZNu411Qwgjv8YssPxEdzXN93hDkSRjLXK8WmfgbmrJW4ZZ3yUPK=w1052-h592-rw

```html
<!DOCTYPE html>
<html lang="en">
<head>
<meta charset="utf-8">
<title>Hypertension, Acute</title>
<link href="https://fonts.googleapis.com/css2?family=Fira+Sans+Condensed:wght@300;400;500;600;700;800&display=swap" rel="stylesheet">
<style>
  :root {
    --brand-blue: #29abe2;
    --panel-grey: #f2f2f2;
    --panel-edge: #d9d9d9;
    --ink: #3a3a3a;
    --ink-strong: #333333;
    --rule: #555555;
    --white: #ffffff;
  }
  * { box-sizing: border-box; margin: 0; padding: 0; }
  html, body { width: 1200px; height: 927px; overflow: hidden; background: var(--white); }
  body { font-family: "Fira Sans Condensed", "Arial Narrow", sans-serif; color: var(--ink); }
  .page { position: relative; width: 1200px; height: 927px; overflow: hidden; }
  .panels { position: absolute; inset: 0; }

  .title-band {
    position: absolute; left: 0; top: 41px; width: 1102px; height: 58px;
    background: var(--brand-blue); border-top-right-radius: 14px;
    box-shadow: 4px 6px 10px rgba(0,0,0,.18);
    display: flex; align-items: baseline; padding-left: 82px; padding-top: 8px;
    color: var(--white);
  }
  .title-band h1 { font-size: 37px; font-weight: 700; letter-spacing: .3px; }
  .title-band p { font-size: 20px; font-weight: 400; margin-left: 6px; }

  .intro { position: absolute; left: 103px; top: 162px; width: 500px; }
  .intro h2 { font-size: 16.5px; font-weight: 700; line-height: 18.5px; text-transform: uppercase; color: var(--ink-strong); }
  .intro ul { list-style: none; margin-top: 8px; font-size: 16px; font-weight: 300; color: var(--ink); }
  .intro li { line-height: 27.5px; }
  .intro li.sub { padding-left: 14px; }

  .range-table {
    position: absolute; left: 611px; top: 157px; width: 446px;
    border-collapse: collapse; text-align: center; background: var(--panel-grey);
  }
  .range-table th, .range-table td { border: 1px solid var(--rule); }
  .range-table .table-title th { background: var(--brand-blue); color: var(--white); height: 30px; font-size: 17.5px; font-weight: 700; }
  .range-table .col-heads th { height: 30px; font-size: 17.5px; font-weight: 700; color: var(--ink-strong); }
  .range-table td { height: 29px; font-size: 16px; font-weight: 300; }
  .range-table col.age { width: 155px; } .range-table col.sys { width: 155px; }

  .caution { position: absolute; left: 120px; top: 320px; width: 925px; text-align: center; font-size: 16px; font-weight: 300; line-height: 20.5px; }
  .caution strong { font-weight: 700; color: var(--ink-strong); }

  .drug-table {
    position: absolute; left: 124px; top: 459px; width: 933px;
    border-collapse: collapse; background: var(--panel-grey);
  }
  .drug-table th, .drug-table td { border: 1px solid var(--rule); vertical-align: top; }
  .drug-table th { background: var(--brand-blue); color: var(--white); height: 30px; font-size: 17.5px; font-weight: 700; text-align: center; vertical-align: middle; }
  .drug-table td.action { width: 297px; padding: 6px 6px 0; font-size: 16px; font-weight: 700; color: var(--ink-strong); line-height: 20px; }
  .drug-table td.drugs { padding: 3px 6px 0; font-size: 16px; font-weight: 300; }
  .drug-table td.drugs ul { list-style: none; }
  .drug-table td.drugs li { line-height: 27.5px; }
  .drug-table tr.pair td { height: 56px; }
  .drug-table tr.single td { height: 29px; }
  .drug-table tr.single td.drugs { padding-top: 0; }
  .drug-table tr.single td.action { padding-top: 4px; }

  .differential {
    position: absolute; left: 132px; top: 754px; width: 937px; height: 96px;
    background: var(--brand-blue); border-radius: 12px 12px 0 12px;
    box-shadow: 0 0 0 3px var(--white), 3px 5px 10px rgba(0,0,0,.22);
    color: var(--white); font-size: 16.5px; font-weight: 500; line-height: 18.2px;
  }
  .differential .col { position: absolute; top: 11px; list-style: none; }
  .differential .col li { padding-left: 13px; text-indent: -13px; }
  .differential .col-a { left: 66px; width: 270px; }
  .differential .col-b { left: 357px; width: 270px; }
  .differential .col-c { left: 648px; width: 260px; }
  .differential h3 { font-size: 16.5px; font-weight: 700; text-indent: 0; padding-left: 0; }

  .revision { position: absolute; right: 127px; top: 885px; font-size: 13px; font-weight: 700; color: var(--ink-strong); }
</style>
</head>
<body>
<main class="page">
  <svg class="panels" width="1200" height="927" viewBox="0 0 1200 927" aria-hidden="true">
    <defs>
      <filter id="panel-shadow" x="-5%" y="-10%" width="110%" height="130%">
        <feDropShadow dx="0" dy="6" stdDeviation="8" flood-color="#000" flood-opacity=".18"/>
      </filter>
    </defs>
    <g filter="url(#panel-shadow)">
      <path fill="var(--brand-blue)" d="M1125 132 Q1145 140 1143 160 L1107 378 Q1098 410 1045 411 L240 411 Q228 411 228 398 L228 390 L1100 390 Z"/>
      <path fill="var(--panel-edge)" d="M60 126 L1110 126 L1080 368 Q1072 396 1030 397 L118 397 Q88 396 84 366 Z"/>
      <path fill="var(--panel-grey)" d="M58 125 L1110 125 Q1112 126 1110 132 L1070 358 Q1065 386 1028 387 L125 387 Q102 386 98 362 Z"/>
    </g>
    <g filter="url(#panel-shadow)">
      <path fill="var(--brand-blue)" d="M1126 448 Q1146 456 1144 476 L1108 694 Q1099 727 1046 728 L240 728 Q228 728 228 715 L228 706 L1100 706 Z"/>
      <path fill="var(--panel-edge)" d="M60 442 L1110 442 L1080 684 Q1072 713 1030 714 L118 714 Q88 713 84 682 Z"/>
      <path fill="var(--panel-grey)" d="M58 441 L1110 441 Q1112 442 1110 448 L1070 674 Q1065 703 1028 704 L125 704 Q102 703 98 678 Z"/>
    </g>
  </svg>

  <header class="title-band">
    <h1>HYPERTENSION, ACUTE</h1>
    <p>Sustained high blood pressure refractory to treating reversible causes</p>
  </header>

  <section class="intro">
    <h2>In pediatrics, hypertension is almost always treated by addressing likely causes such as light anesthesia or measurement error:</h2>
    <ul>
      <li>• Ensure correct BP cuff size: cuff bladder width ~ 40% of limb circumference</li>
      <li>• Ensure arterial line transducer is at level of heart</li>
      <li class="sub">- Consider placing arterial line if not already present</li>
    </ul>
  </section>

  <table class="range-table">
    <colgroup><col class="age"><col class="sys"><col class="dia"></colgroup>
    <tr class="table-title"><th colspan="3">HYPERTENSIVE BLOOD PRESSURE RANGE*</th></tr>
    <tr class="col-heads"><th>AGE (YR)</th><th>SYSTOLIC</th><th>DIASTOLIC</th></tr>
    <tr><td>newborn</td><td>&gt;97</td><td>&gt;70</td></tr>
    <tr><td>1-3</td><td>&gt;105</td><td>&gt;61</td></tr>
    <tr><td>4-12</td><td>&gt;113</td><td>&gt;86</td></tr>
  </table>

  <p class="caution"><strong>*CAUTION:</strong> Anti-hypertensive drugs are almost never needed for routine pediatric cases. These medications are used almost exclusively for specialized cardiac, neurosurgical, or endocrine (pheochromocytoma) cases. Consult an expert before use. Rule-out increased ICP.</p>

  <table class="drug-table">
    <tr><th>ACTION</th><th>DRUG (IV DOSING)</th></tr>
    <tr class="pair">
      <td class="action">Direct smooth muscle relaxation</td>
      <td class="drugs"><ul>
        <li>• Sodium nitroprusside 0.5-10 MICROgrams/kg/min</li>
        <li>• HydrALAZINE 0.1-0.2 mg/kg (adult dose 5-10 mg)</li>
      </ul></td>
    </tr>
    <tr class="pair">
      <td class="action">β -Adrenergic blockade</td>
      <td class="drugs"><ul>
        <li>• Esmolol 100-500 MICROgrams/kg over 5 min, then 25-300 MICROgrams/kg/min</li>
        <li>• Labetalol (also a effect) 0.2-1 mg/kg q 10 min; 0.4-3 mg/kg/hour (infusion)</li>
      </ul></td>
    </tr>
    <tr class="pair">
      <td class="action">Calcium channel blockade</td>
      <td class="drugs"><ul>
        <li>• niCARdapine 0.5-5 MICROgrams/kg/min</li>
        <li>• Clevidipine 0.5-3.5 MICROgrams/kg/min</li>
      </ul></td>
    </tr>
    <tr class="single">
      <td class="action">D1-dopamine agonist</td>
      <td class="drugs"><ul><li>• Fenoldopam 0.2-0.8 MICROgrams/kg/min</li></ul></td>
    </tr>
  </table>

  <section class="differential">
    <ul class="col col-a">
      <li><h3>CONSIDER DIFFERENTIAL (PARTIAL):</h3></li>
      <li>• Light anesthesia (consider vaporizer or infusion pump empty or malfunctioning)</li>
    </ul>
    <ul class="col col-b">
      <li>• Hypercarbia</li>
      <li>• Hypoxemia</li>
      <li>• Arterial line transducer too low or BP cuff too smal</li>
    </ul>
    <ul class="col col-c">
      <li>• Withdrawal (EtOH or opioid)</li>
      <li>• Thyroid Storm</li>
      <li>• Pheochromocytoma</li>
      <li>• Drug Error</li>
    </ul>
  </section>

  <p class="revision">REVISION OCTOBER 2023</p>
</main>
</body>
</html>
```